Leading inbound Tour Operator Silver Maple Voyage needs an e-mail newsletter design and html template

Introduction
We need a newsletter design for a experienced tour-company based in Los Angeles called Silver Maple Voyage Inc www.silvermaplevoyage.com. We are leading inbound Tour Operator, serving Russian-speaking travelers in North America, and we are in business for over 14 years. We provide travel services to our customers including professional tour guide services on East coast and West Coast, coach bus-tours, private transportation, and much more.

Technical specifications for production design html-template of 2 types e-mail-newsletters in russian language.

Company Name
Silver Maple Voyage Inc http://silvermaplevoyage.com

Goal
To increase the involvement of Target Audience in the interaction with the brand, increase loyalty, increase interest in the services of the company, increasing the number of tour and services orders. This is why we use direct mail as one of major marketing instruments. This e-mail html template should be constructed the way allowing us to change pictures and texts. It means that we need reusable templates.

Target Audience:
• 1st design template - business partners. Agencies and tour operators from Russia (Moscow, St. Petersburg, Yekaterinburg) and other Russian-language countries: Ukraine, Belarus, Bulgaria, Latvia. It is the middle-class audience, mostly female, professionals in tourism sphere
• 2nd design template -direct customers. Travelers from former CIS countries: Ukrainian 2/3, Russian 1/3 part. Men and women, middle age (35 years and older), in managerial positions in big companies, have average or above average income, modern and active lifestyle, love to travel and learn new things.

Object of advertising
Multi-day bus tours of the East and West Coast USA.
Examples of tours advertised in the newsletter:
• Canyon Ribbon Journey VIP – http://silvermaplevoyage.ru/en/tours/wonders-of-the-southwest-vip/
• Canyon Ribbon Journey – http://silvermaplevoyage.ru/en/tours/wonders-of-the-southwest-11-days/
• Coast to Coast Loop – http://silvermaplevoyage.ru/en/tours/all-america/
• East Coast and Canada - http://silvermaplevoyage.ru/en/tours/east-coast-and-canada-11-days/
• Los Angeles Grand-tour - http://silvermaplevoyage.ru/en/tours/los-angeles-grand-tour/
• Tour to Las Vegas - http://silvermaplevoyage.ru/en/tours/las-vegas-2-days/

Description of the advertised tour
Multi-day bus tours for 50 people. Cost is average. The tour price includes: transfers between cities, excursions along the route, DBL hotel accommodation and breakfasts.

This is important
There is a lot of e-mails everyday sent about tourism, our goal is to stand out of the competitors, and to present company’s service clear and understandable, engaging and interesting at the same time.

Corporate Identity
Color: gold (5/29/100/0), red (14/99/100/0) combined with black / white.
Font: Century Gothic Helvetica OR
Company’s Symbol: Star in the logo (image attached).

Our wishes to the e-mail structure
(Please be advised that the order of the blocks is not required. We would like to get vision of the designer – the best way to present information).
• Block 1 - Contact and logo
• Block 2 – Introductory text ( useful information like news update about USA or any other interesting up-to-date fact catching the eye of the audience) and an important message from the president (including pictures and sign)
• Block 3 - Information about the most important tour in this period of time. This unit should be the most important in the layout, emotionally isolated and eye-catching.
• Block 3 – 6 - scheduled tours or excursions. It is important that the information was easily readable and drawing the attention.

Design difference between 2 types of e-mails
• the 1st design template – for business partners. It should has a table structure, to be very simple and readable even if we will show up to 8 type of tours. So the main descriptions of this template is tabular
• the 2nd design template – for direct customers. It should have the unique and interesting element, which will draw clients’ attention so they wish to read our e-mail from the beginning to the end.

Email size
No larger than 600 px. in width and no more than 2 screens.

Design our previous emails
http://mail.pelnorix-archive.com/?u=7a2c91e0f4b3d6a8c5e1f9207&id=c8d1e0a2f3
http://mail.pelnorix-archive.com/?u=7a2c91e0f4b3d6a8c5e1f9207&id=d4a7b9e6c1

• Examples of e-mails that we like PLUS: http://r.quavelto.com/V7P/mv.aspx?k=tRbWkeLpZx2mmQsc8gh3HH41plQdfnuaXkBT7K-3D8FxVyTbNrsLPRQ$$
http://brenwickfund.trelmail.com/t/ViewEmail/j/8A14F7E2B09D35C1/5E9B2C7D41A086F3E2D19B7CA40E6F58

Text for use in e-mail

Contacts
Теl. +1 (800) 555-0148
Skype silver_maple3816
E-mail info@silvermaplevoyage.com

Social networks widgets:
Facebook - https://www.facebook.com/silvermaplevoyage.ru
Vkontakte - http://vk.com/silvermaplevoyage
Instagram - http://instagram.com/silvermaplevoyage
Twitter - https://twitter.com/SilverMapleVoyage
Vidora -https://www.youtube.com/channel/UCq7TM3P2wnhRdX_oKLzWbVa

Introductory text
«Добрый день!

В США прибыла рекордная группа туристов из Китая. Количество путешественников превысело 6 000 человек! Что же привлекает в Америке путешественников со всего мира? Вы можете увидеть и оценить главные достопримечательности Запада Америки на нашем официальном видео-канале на Vidora. Приятного просмотра!

C уважением, Олег Кузьмин
президент компании Silver Maple Voyage Inc.»

Description of main advertise tour
Picture, Name, Dates, Cost, Duration, Itinerary, Link to site «View»

«Каньонное кольцо США

Даты заездов 12.09, 03.10, 31.10
Продолжительность 11 дней
Стоимость на чел. $ 1 495

Программа Санта-Барбара - Сан-Франциско - Йосемити - Лас-Вегас - Долина Смерти - каньон Антилопы - трасса 66 - Гранд Каньон - Сан-Диего - Лос-Анджелес
Узнать подробнее»

Scheduled tours or excursions
Name of this block – РАСПИСАНИЕ ТУРОВ SILVER MAPLE VOYAGE
Description for each tours – Picture, Date, Name, Cost, Duration, Link to site «View»
«08.06
Лос-Анджелес
$ 95 / 6 часов
Подробнее»

```html
<!DOCTYPE html>
<html lang="ru">
<head>
<meta charset="utf-8">
<title>Silver Maple Voyage — рассылка</title>
<link href="https://fonts.googleapis.com/css2?family=Open+Sans:wght@400;600;700;800&display=swap" rel="stylesheet">
<style>
:root{
  --cream:#f1e9cf;
  --paper:#ffffff;
  --red:#d7191f;
  --red-dark:#a8121a;
  --gold:#f4b51b;
  --ink:#1b1b1b;
  --muted:#555;
  --chip:#f3ecd6;
  --link:#1a2fc9;
}
*{box-sizing:border-box;margin:0;padding:0}
html,body{width:1200px;height:1100px;overflow:hidden}
body{background:var(--cream);font-family:"Open Sans",Arial,sans-serif;color:var(--ink);position:relative}
.email{position:absolute;left:425px;top:24px;width:350px;height:940px;background:var(--paper)}
.email > *{position:absolute}
.logo{left:6px;top:19px;display:flex;align-items:center;gap:4px;white-space:nowrap}
.logo-dot{width:14px;height:14px;border-radius:50%;background:var(--gold)}
.logo-name{font-size:11px;font-weight:600;color:var(--ink);letter-spacing:-.2px}
.date-tag{left:142px;top:23px;width:62px;height:15px;background:var(--red);color:#fff;font-size:5.6px;font-weight:700;display:flex;align-items:center;justify-content:center;white-space:nowrap}
.contacts{left:234px;top:8px;font-size:5.3px;line-height:12px;display:grid;grid-template-columns:20px auto;white-space:nowrap}
.contacts dt{color:var(--red)}
.contacts dd{font-weight:700}
.hero{left:9px;top:57px;width:330px;height:121px;background:linear-gradient(180deg,#4a5570 0%,#6b7590 40%,#2b3040 100%);overflow:hidden}
.hero-curve{position:absolute;left:0;bottom:0;width:330px;height:16px}
.slogan{left:222px;top:48px;width:117px;height:84px}
.slogan-text{position:absolute;left:0;top:0;width:117px;height:58px;padding:7px 10px;color:#fff;font-size:7px;line-height:8.5px}
.slogan-text strong{display:block;font-size:9.5px;line-height:10.5px;font-weight:800}
.intro{left:9px;top:184px;width:330px;font-size:6px;line-height:9.4px}
.intro h1{font-size:6.2px;font-weight:700}
.intro a{color:var(--link)}
.avatar{left:9px;top:241px;width:39px;height:39px;border-radius:50%;background:radial-gradient(circle,#8c93a3,#2f3545);border:2px solid #d9d9d9}
.signature{left:52px;top:244px;width:100px;height:24px;background:linear-gradient(90deg,#ededed,#f7f7f7)}
.signer{left:52px;top:271px;font-size:5.6px;white-space:nowrap}
.banner{left:9px;top:299px;width:330px;height:107px;border-top:2px solid var(--red);background:linear-gradient(90deg,#c45a2f 0%,#e2a265 25%,#6d93c2 45%,#e7b34c 68%,#7fa0b5 85%,#c8a566 100%)}
.banner-title{left:202px;top:378px;width:137px;height:13px;background:var(--red);color:#fff;font-size:7.2px;font-weight:800;display:flex;align-items:center;padding-left:4px;white-space:nowrap}
.banner-sub{left:202px;top:391px;width:86px;height:12px;background:var(--gold);color:var(--ink);font-size:7.2px;font-weight:800;display:flex;align-items:center;padding-left:4px;white-space:nowrap}
.banner-base{left:9px;top:404px;width:330px;height:2px;background:var(--gold)}
.details{left:9px;top:412px;width:330px;font-size:6px;line-height:9.4px}
.details b{font-weight:700}
.price{color:var(--red);font-weight:700}
.more{display:flex;align-items:center;height:13px;color:var(--ink);text-decoration:none}
.more-icon{width:13px;height:13px;background:var(--red);display:flex;align-items:center;justify-content:center}
.more-label{height:11px;background:var(--chip);font-size:5.5px;font-weight:600;padding:0 5px;display:flex;align-items:center;border-radius:0 3px 3px 0}
.photo{overflow:hidden}
.ph-town{background:linear-gradient(180deg,#2f6cc6 0%,#7aa6e0 45%,#a0563c 70%,#6a4a36 100%)}
.ph-hotel{background:linear-gradient(180deg,#3f79c9 0%,#b9cfe6 45%,#d6c18e 65%,#4e7f8a 100%)}
.ph-palms{background:linear-gradient(180deg,#3a6fc0,#8fb5e0 60%,#33572f)}
.ph-sign{background:linear-gradient(160deg,#8e8e8e,#4a4a4a 60%,#6c6c6c)}
.ph-truck{background:linear-gradient(180deg,#6e9fd4,#c9884a 60%,#5a4a3a)}
.ph-capitol{background:linear-gradient(180deg,#2c5fb8,#8fb4e6 55%,#e8e8e8 80%,#4d7a3c)}
.ph-church{background:linear-gradient(180deg,#3c73c7,#9fbde4 40%,#c8c0b0 70%,#7d7466)}
.ph-vine{background:linear-gradient(180deg,#cfe6a3,#6fa83d 55%,#2f5c1e)}
.vip{position:absolute;right:5px;top:5px;width:50px;height:50px;border-radius:50%;background:var(--red);color:#fff;display:flex;flex-direction:column;align-items:center;justify-content:center;font-weight:800;line-height:1}
.vip span:first-child{font-size:12px}
.vip span:last-child{font-size:6.5px;margin-top:1px}
.card-text{font-size:5.8px;line-height:10px;white-space:nowrap}
.card-text b{font-weight:700}
.footer{position:absolute;left:0;width:1200px;top:970px;text-align:center;font-size:5.3px;line-height:8.8px;color:var(--muted)}
.footer strong{color:#333}
.social{display:flex;justify-content:center;gap:2px;margin:9px 0 8px}
.social span{width:13px;height:13px;border-radius:50%;background:#111}
.footer a{color:var(--link)}
</style>
</head>
<body>
<main class="email">
  <div class="logo"><span class="logo-dot"></span><span class="logo-name">Silver Maple Voyage</span></div>
  <div class="date-tag">15 - 21 July 2014</div>
  <dl class="contacts">
    <dt>Тел.:</dt><dd>+1 (800) 555-0148</dd>
    <dt>Skype:</dt><dd>silver_maple3816</dd>
    <dt>E-mail:</dt><dd>info@silvermaplevoyage.com</dd>
  </dl>

  <div class="hero" role="img" aria-label="Ночной вид небоскрёбов большого города">
    <svg class="hero-curve" viewBox="0 0 330 16" preserveAspectRatio="none"><path d="M0 6 Q165 20 330 4 L330 16 L0 16Z" fill="#fff"/><path d="M0 6 Q165 20 330 4" stroke="#d7191f" stroke-width="3" fill="none"/></svg>
  </div>
  <div class="slogan">
    <svg width="117" height="84" viewBox="0 0 117 84"><rect width="117" height="58" fill="#d7191f"/><path d="M0 58 L117 58 L117 72 L40 78 L14 84 L22 70 Z" fill="#d7191f"/><path d="M0 58 L22 70 L14 84 Z" fill="#a8121a"/></svg>
    <p class="slogan-text">YOUR NICE WEEKLY<strong>CAMPAIGN<br>SLOGAN</strong>COULD BE PLACED HERE</p>
  </div>

  <section class="intro">
    <h1>Добрый день!</h1>
    <p>В США прибыла рекордная группа туристов из Китая. Количество путешественников превысело 6 000 человек! Что же привлекает в Америке путешественников со всего мира? Вы можете увидеть и оценить <b>главные достопримечательности Запада Америки</b> на нашем официальном <a href="#">видео-канале на Vidora.</a></p>
    <p>Приятного просмотра!</p>
    <p>С уважением,</p>
  </section>
  <div class="avatar" role="img" aria-label="Портрет президента компании"></div>
  <div class="signature" role="img" aria-label="Подпись президента"></div>
  <p class="signer"><b>Олег Кузьмин</b>, президент компании Silver Maple Voyage Inc.</p>

  <div class="banner" role="img" aria-label="Коллаж: мост на закате, небоскрёбы, вывеска Лас-Вегаса, статуя Свободы"></div>
  <div class="banner-base"></div>
  <div class="banner-title">КАНЬОННОЕ КОЛЬЦО США</div>
  <div class="banner-sub">АВТОБУСНЫЙ ТУР</div>

  <section class="details">
    <p>Даты заездов: <b>12.09, 03.10, 31.10 27.06, 25.07, 08.08</b></p>
    <p>Продолжительность: <b>11 дней</b></p>
    <p>Стоимость на чел.: <span class="price">1,495 $</span></p>
    <p>Программа: <b>Санта-Барбара - Сан-Франциско - Йосемити - Лас-Вегас - Долина Смерти - каньон Антилопы - трасса 66 - Гранд Каньон - Сан-Диего - Лос-Анджелес</b></p>
  </section>
  <a class="more" href="#" style="left:9px;top:464px"><span class="more-icon"><svg width="7" height="7" viewBox="0 0 7 7"><path d="M2 1l3 2.5L2 6" stroke="#fff" stroke-width="1.4" fill="none"/></svg></span><span class="more-label">Подробнее</span></a>

  <div class="photo ph-town" role="img" aria-label="Фахверковые дома в городке" style="left:9px;top:492px;width:160px;height:101px"><div class="vip"><span>VIP</span><span>PACKAGE</span></div></div>
  <div class="photo ph-hotel" role="img" aria-label="Отель у фонтанов в Лас-Вегасе" style="left:180px;top:492px;width:159px;height:101px"></div>
  <div class="card-text" style="left:9px;top:598px">27.06, 25.07, 08.08 | <b>Западный Мираж</b><br><span class="price">95 $</span> / 6 часов</div>
  <div class="card-text" style="left:180px;top:598px">27.06, 25.07 | <b>Каньонное кольцо VIP-тур</b><br><span class="price">2,395 $</span> / 11 дней</div>
  <a class="more" href="#" style="left:9px;top:628px"><span class="more-icon"><svg width="7" height="7" viewBox="0 0 7 7"><path d="M2 1l3 2.5L2 6" stroke="#fff" stroke-width="1.4" fill="none"/></svg></span><span class="more-label">Подробнее</span></a>
  <a class="more" href="#" style="left:180px;top:628px"><span class="more-icon"><svg width="7" height="7" viewBox="0 0 7 7"><path d="M2 1l3 2.5L2 6" stroke="#fff" stroke-width="1.4" fill="none"/></svg></span><span class="more-label">Подробнее</span></a>

  <div class="photo ph-palms" role="img" aria-label="Пальмы и дорожные указатели" style="left:9px;top:656px;width:76px;height:54px"></div>
  <div class="photo ph-sign" role="img" aria-label="Уличный указатель" style="left:89px;top:656px;width:76px;height:54px"></div>
  <div class="photo ph-truck" role="img" aria-label="Старый грузовик на трассе" style="left:179px;top:656px;width:76px;height:54px"></div>
  <div class="photo ph-capitol" role="img" aria-label="Здание Капитолия" style="left:260px;top:656px;width:79px;height:54px"></div>
  <div class="card-text" style="left:9px;top:714px">24.06<br><b>Лос-Анджелес</b><br><span class="price">95 $</span> / 6 часов</div>
  <div class="card-text" style="left:89px;top:714px">30.09<br><b>Восток Канада</b><br><span class="price">1,095 $</span> / 14 дней</div>
  <div class="card-text" style="left:179px;top:714px">20.10<br><b>Тур "Coast to Coast Loop"</b><br><span class="price">1,995 $</span> / 14 дней</div>
  <div class="card-text" style="left:260px;top:714px">24.12<br><b>Лас-Вегас</b><br><span class="price">895 $</span> / 4 дней</div>
  <a class="more" href="#" style="left:9px;top:748px"><span class="more-icon"><svg width="7" height="7" viewBox="0 0 7 7"><path d="M2 1l3 2.5L2 6" stroke="#fff" stroke-width="1.4" fill="none"/></svg></span><span class="more-label">Подробнее</span></a>
  <a class="more" href="#" style="left:89px;top:748px"><span class="more-icon"><svg width="7" height="7" viewBox="0 0 7 7"><path d="M2 1l3 2.5L2 6" stroke="#fff" stroke-width="1.4" fill="none"/></svg></span><span class="more-label">Подробнее</span></a>
  <a class="more" href="#" style="left:179px;top:748px"><span class="more-icon"><svg width="7" height="7" viewBox="0 0 7 7"><path d="M2 1l3 2.5L2 6" stroke="#fff" stroke-width="1.4" fill="none"/></svg></span><span class="more-label">Подробнее</span></a>
  <a class="more" href="#" style="left:260px;top:748px"><span class="more-icon"><svg width="7" height="7" viewBox="0 0 7 7"><path d="M2 1l3 2.5L2 6" stroke="#fff" stroke-width="1.4" fill="none"/></svg></span><span class="more-label">Подробнее</span></a>

  <div class="photo ph-church" role="img" aria-label="Купол собора среди небоскрёбов" style="left:9px;top:777px;width:160px;height:101px"></div>
  <div class="photo ph-vine" role="img" aria-label="Бокал вина на фоне виноградника" style="left:180px;top:777px;width:159px;height:101px"></div>
  <div class="card-text" style="left:9px;top:883px">27.06, 25.07, 08.08 | <b>Западный Мираж</b><br><span class="price">95 $</span> / 6 часов</div>
  <div class="card-text" style="left:180px;top:883px">27.06, 25.07 | <b>Каньонное кольцо VIP-тур</b><br><span class="price">2,395 $</span> / 11 дней</div>
  <a class="more" href="#" style="left:9px;top:912px"><span class="more-icon"><svg width="7" height="7" viewBox="0 0 7 7"><path d="M2 1l3 2.5L2 6" stroke="#fff" stroke-width="1.4" fill="none"/></svg></span><span class="more-label">Подробнее</span></a>
  <a class="more" href="#" style="left:180px;top:912px"><span class="more-icon"><svg width="7" height="7" viewBox="0 0 7 7"><path d="M2 1l3 2.5L2 6" stroke="#fff" stroke-width="1.4" fill="none"/></svg></span><span class="more-label">Подробнее</span></a>
</main>

<footer class="footer">
  <p><strong>Silver Maple Voyage Inc.</strong></p>
  <p>4120 W. Ridgeview Ave. Suite 310 · Glendale · CA 91203</p>
  <p>toll free 1.800.555.0148 · office 323.555.0192 · fax 323.555.0177</p>
  <div class="social"><span></span><span></span><span></span><span></span><span></span></div>
  <p>Copyright © 2014 Silver Maple Voyage, Inc., All rights reserved.</p>
  <p>Вы получили данный e-mail, потому что находитесь в нашей базе данных.</p>
  <p>Если вы больше не хотите получать нашу рассылку, пожалуйста, нажмите <a href="#">отписаться от рассылки</a></p>
</footer>
</body>
</html>
```